Awesome Professional Template for a collaborative report

File format: A4 PDF ideally

Design Requirements:

3 or 4 variants of a template some with graphics and pull quotes and a bio page for the essayists with a profile pic and a short descriptor

Layout Format: PPT would be perfect ideally portrait format

Style/Reference Guide: Varnholt or QP styles thought leadership reports as a guide

We need to input 10 essays around a specific subject with a nice layout with place holders for high impact pull quotes from the copy, stunning colourway and typrography probably A4 format but emailed as a PDF ideally not a huge file size. Striking front cover with title and list of contributors plus layout variations for the essays which will include a head shot short profile and contacts for the authors. Ideally a portrait format PPT that is easy to work with.

Target Market(s)

business professionals in brands

Industry/Entity Type

brand marketing

Font styles to use
Sans Serif

Colors
0054AA
0677BA
7BADD7
CADEEF
E8F1F8
00AB8E
00BBA5
67D7C9
C6EFE9
E9F9F6
F0912C
F2A743
F7CA91
FBE8D2
FDF5EE
6B429C
8869AF
B7A5CE
E3DAEB
F3F0F8

Requirements
Must have
• awesome visual impact

```html
<!DOCTYPE html>
<html lang="en">
<head>
<meta charset="utf-8">
<title>The Truth About AI – Report Template Spreads</title>
<link rel="stylesheet" href="https://fonts.googleapis.com/css2?family=Poppins:ital,wght@0,500;0,600;0,700;0,800;1,600;1,700;1,800&family=Open+Sans:wght@400;600&display=swap">
<style>
  :root {
    --ink: #111318;
    --body: #4a4f57;
    --muted: #8a9099;
    --orange: #F0912C;
    --orange-soft: #FBE8D2;
    --navy: #06122e;
    --blue-deep: #0054AA;
    --blue: #0677BA;
    --blue-light: #7BADD7;
    --cyan: #67D7C9;
    --paper: #ffffff;
    --canvas: #e9ecf0;
  }
  * { box-sizing: border-box; margin: 0; padding: 0; }
  html, body { width: 1200px; height: 2400px; overflow: hidden; background: var(--canvas); }
  body { font-family: "Open Sans", Arial, sans-serif; color: var(--body); }

  .spreads { display: grid; grid-template-columns: repeat(3, 392px); column-gap: 12px; row-gap: 12px; width: 1200px; }
  .page { position: relative; background: var(--paper); overflow: hidden; }
  .row-1 { height: 670px; }
  .row-2 { height: 680px; }
  .row-3 { height: 660px; }
  .row-4 { height: 354px; }

  .photo { position: absolute; background: linear-gradient(140deg, var(--navy) 0%, var(--blue-deep) 45%, var(--blue) 70%, var(--cyan) 100%); }
  .photo.soft { background: radial-gradient(circle at 55% 40%, #cfe8f7 0%, var(--blue-light) 35%, var(--blue) 65%, var(--navy) 100%); }
  .photo.dark { background: linear-gradient(160deg, #02081c 0%, #0a2a66 55%, #1a6fb8 100%); }
  .photo.round { border-radius: 50%; }

  .cover-title { position: absolute; left: 20px; top: 18px; font-family: "Poppins", Arial, sans-serif; font-weight: 500; font-size: 46px; line-height: 1.08; color: var(--ink); }
  .cover-title .accent { color: var(--orange); display: block; }

  .contributors { position: absolute; left: 22px; top: 140px; display: grid; grid-template-columns: repeat(3, 34px); gap: 12px 10px; }
  .avatar { width: 34px; height: 34px; border-radius: 50%; background: radial-gradient(circle at 50% 35%, #f3c9a6 0%, #b2473a 60%, #5d1e22 100%); }

  .chapter-no { position: absolute; left: 24px; top: 18px; width: 58px; height: 52px; background: var(--orange); color: #fff; font-family: "Poppins", Arial, sans-serif; font-weight: 700; font-size: 30px; display: flex; align-items: center; justify-content: center; }
  .essay-title { position: absolute; left: 24px; top: 84px; width: 330px; font-family: "Poppins", Arial, sans-serif; font-weight: 700; font-size: 33px; line-height: 1.12; color: var(--ink); }
  .author { position: absolute; left: 24px; top: 262px; width: 150px; text-align: center; }
  .author .portrait { position: relative; width: 110px; height: 110px; margin: 0 auto; border-radius: 50%; background: radial-gradient(circle at 50% 40%, #f0c2a0 0%, #a3412f 55%, #4a1a1f 100%); }
  .author-name { margin-top: 8px; background: var(--orange); color: #fff; font-family: "Poppins", Arial, sans-serif; font-weight: 600; font-size: 11px; padding: 4px 6px; }
  .author-bio { margin-top: 5px; font-size: 6.5px; line-height: 1.45; color: var(--body); }

  .heading { position: absolute; font-family: "Poppins", Arial, sans-serif; font-weight: 700; color: var(--ink); }
  .heading.lg { font-size: 24px; }
  .subhead { font-family: "Poppins", Arial, sans-serif; font-style: italic; font-weight: 700; font-size: 10px; color: var(--ink); margin-bottom: 6px; }

  .col { position: absolute; font-size: 6.6px; line-height: 1.55; color: var(--body); }
  .col p { margin-bottom: 7px; }

  .contents-title { position: absolute; left: 0; right: 0; top: 130px; text-align: center; font-family: "Poppins", Arial, sans-serif; font-weight: 800; font-size: 30px; letter-spacing: 1px; color: var(--ink); }
  .toc { position: absolute; left: 64px; top: 212px; list-style: none; }
  .toc li { display: flex; align-items: baseline; gap: 12px; height: 38px; }
  .toc .num { font-family: "Poppins", Arial, sans-serif; font-style: italic; font-weight: 800; font-size: 17px; color: var(--ink); width: 28px; }
  .toc .label { font-family: "Poppins", Arial, sans-serif; font-weight: 600; font-size: 8px; letter-spacing: 1px; color: var(--ink); }
  .toc .dots { font-size: 8px; color: var(--muted); letter-spacing: 2px; }

  .pull-quote { position: absolute; left: 178px; top: 50px; width: 196px; font-family: "Poppins", Arial, sans-serif; font-style: italic; font-weight: 800; font-size: 13.5px; line-height: 1.35; text-transform: uppercase; color: var(--ink); }

  .footer { position: absolute; left: 20px; right: 20px; bottom: 12px; display: flex; justify-content: space-between; align-items: center; font-size: 5.5px; color: var(--muted); }
  .footer .dot { width: 12px; height: 12px; border-radius: 50%; background: var(--navy); box-shadow: 0 0 0 3px #9bc3e4; }
</style>
</head>
<body>
<main class="spreads">

  <!-- Row 1 -->
  <section class="page row-1 cover cover-contributors">
    <h1 class="cover-title">The Truth <span class="accent">About AI</span></h1>
    <div class="contributors" aria-label="Contributors">
      <div class="avatar" role="img" aria-label="Contributor headshot"></div>
      <div class="avatar" role="img" aria-label="Contributor headshot"></div>
      <div class="avatar" role="img" aria-label="Contributor headshot"></div>
      <div class="avatar" role="img" aria-label="Contributor headshot"></div>
      <div class="avatar" role="img" aria-label="Contributor headshot"></div>
      <div class="avatar" role="img" aria-label="Contributor headshot"></div>
      <div class="avatar" role="img" aria-label="Contributor headshot"></div>
      <div class="avatar" role="img" aria-label="Contributor headshot"></div>
      <div class="avatar" role="img" aria-label="Contributor headshot"></div>
      <div class="avatar" role="img" aria-label="Contributor headshot"></div>
      <div class="avatar" role="img" aria-label="Contributor headshot"></div>
      <div class="avatar" role="img" aria-label="Contributor headshot"></div>
    </div>
    <div class="photo soft" role="img" aria-label="Glowing digital human head illustration" style="left:70px; top:300px; width:322px; height:370px; border-top-left-radius:60% 45%;"></div>
  </section>

  <section class="page row-1 cover cover-image">
    <h1 class="cover-title">The Truth <span class="accent">About AI</span></h1>
    <div class="photo" role="img" aria-label="Abstract network of light and data lines" style="left:0; top:150px; width:392px; height:520px;"></div>
  </section>

  <section class="page row-1 essay-opener">
    <div class="chapter-no">01</div>
    <h2 class="essay-title">Title of The Essay Goes Here</h2>
    <div class="author">
      <div class="portrait" role="img" aria-label="Author headshot"></div>
      <div class="author-name">Author Name</div>
      <p class="author-bio">Strategy lead with fifteen years in brand and digital transformation.</p>
    </div>
    <div class="col" style="left:190px; top:270px; width:180px;">
      <p>Brand leaders are rethinking how they plan, create and measure work as machine learning tools move from pilot projects into daily practice. This section outlines what has changed, where the gains are real and which questions teams should ask before they scale new tools across the business.</p>
      <p>Early adopters report faster turnaround and sharper insight, yet they also stress the need for clear review steps, shared guidelines and human judgement at every stage.</p>
    </div>
    <div class="col" style="left:24px; top:470px; width:165px;">
      <p>Brand leaders are rethinking how they plan, create and measure work as machine learning tools move from pilot projects into daily practice. This section outlines what has changed, where the gains are real and which questions teams should ask before they scale new tools across the business.</p>
    </div>
    <div class="col" style="left:205px; top:470px; width:165px;">
      <p>Early adopters report faster turnaround and sharper insight, yet they also stress the need for clear review steps, shared guidelines and human judgement at every stage.</p>
      <p>Early adopters report faster turnaround and sharper insight, yet they also stress the need for clear review steps, shared guidelines and human judgement at every stage.</p>
    </div>
    <footer class="footer"><span>The Truth About AI · Collaborative Report</span><span class="dot"></span></footer>
  </section>

  <!-- Row 2 -->
  <section class="page row-2 contents">
    <h2 class="contents-title">Contents</h2>
    <ol class="toc">
      <li><span class="num">01</span><span class="label">CHAPTER TITLE</span><span class="dots">..........</span></li>
      <li><span class="num">02</span><span class="label">CHAPTER TITLE</span><span class="dots">..........</span></li>
      <li><span class="num">03</span><span class="label">CHAPTER TITLE</span><span class="dots">..........</span></li>
      <li><span class="num">04</span><span class="label">CHAPTER TITLE</span><span class="dots">..........</span></li>
      <li><span class="num">05</span><span class="label">CHAPTER TITLE</span><span class="dots">..........</span></li>
      <li><span class="num">06</span><span class="label">CHAPTER TITLE</span><span class="dots">..........</span></li>
      <li><span class="num">07</span><span class="label">CHAPTER TITLE</span><span class="dots">..........</span></li>
      <li><span class="num">08</span><span class="label">CHAPTER TITLE</span><span class="dots">..........</span></li>
    </ol>
    <footer class="footer"><span>The Truth About AI · Collaborative Report</span><span class="dot"></span></footer>
  </section>

  <section class="page row-2 introduction">
    <div class="photo" role="img" aria-label="Glowing circuit brain visual" style="left:0; top:0; width:150px; height:250px;"></div>
    <h2 class="heading lg" style="left:170px; top:28px;">Introduction</h2>
    <div class="col" style="left:170px; top:76px; width:200px;">
      <p>Brand leaders are rethinking how they plan, create and measure work as machine learning tools move from pilot projects into daily practice. This section outlines what has changed, where the gains are real and which questions teams should ask before they scale new tools across the business.</p>
      <p>Early adopters report faster turnaround and sharper insight, yet they also stress the need for clear review steps, shared guidelines and human judgement at every stage.</p>
      <p>Brand leaders are rethinking how they plan, create and measure work as machine learning tools move from pilot projects into daily practice. This section outlines what has changed, where the gains are real and which questions teams should ask before they scale new tools across the business.</p>
    </div>
    <div class="col" style="left:20px; top:270px; width:130px;">
      <p>Early adopters report faster turnaround and sharper insight, yet they also stress the need for clear review steps, shared guidelines and human judgement at every stage.</p>
      <p>Brand leaders are rethinking how they plan, create and measure work as machine learning tools move from pilot projects into daily practice. This section outlines what has changed, where the gains are real and which questions teams should ask before they scale new tools across the business.</p>
      <p>Early adopters report faster turnaround and sharper insight, yet they also stress the need for clear review steps, shared guidelines and human judgement at every stage.</p>
    </div>
    <div class="photo" role="img" aria-label="Hand touching a digital interface" style="left:170px; top:330px; width:222px; height:150px;"></div>
    <div class="col" style="left:170px; top:500px; width:200px;">
      <p>Early adopters report faster turnaround and sharper insight, yet they also stress the need for clear review steps, shared guidelines and human judgement at every stage.</p>
    </div>
    <footer class="footer"><span>The Truth About AI · Collaborative Report</span><span class="dot"></span></footer>
  </section>

  <section class="page row-2 title-page">
    <h2 class="heading lg" style="left:24px; top:28px;">Title Here</h2>
    <div class="col" style="left:24px; top:80px; width:344px;">
      <p>Brand leaders are rethinking how they plan, create and measure work as machine learning tools move from pilot projects into daily practice. This section outlines what has changed, where the gains are real and which questions teams should ask before they scale new tools across the business.</p>
      <p>Early adopters report faster turnaround and sharper insight, yet they also stress the need for clear review steps, shared guidelines and human judgement at every stage.</p>
      <p>Brand leaders are rethinking how they plan, create and measure work as machine learning tools move from pilot projects into daily practice. This section outlines what has changed, where the gains are real and which questions teams should ask before they scale new tools across the business.</p>
      <p>Early adopters report faster turnaround and sharper insight, yet they also stress the need for clear review steps, shared guidelines and human judgement at every stage.</p>
    </div>
    <div class="col" style="left:24px; top:300px; width:160px;">
      <p>Brand leaders are rethinking how they plan, create and measure work as machine learning tools move from pilot projects into daily practice. This section outlines what has changed, where the gains are real and which questions teams should ask before they scale new tools across the business.</p>
      <p>Early adopters report faster turnaround and sharper insight, yet they also stress the need for clear review steps, shared guidelines and human judgement at every stage.</p>
    </div>
    <div class="col" style="left:208px; top:300px; width:160px;">
      <p>Brand leaders are rethinking how they plan, create and measure work as machine learning tools move from pilot projects into daily practice. This section outlines what has changed, where the gains are real and which questions teams should ask before they scale new tools across the business.</p>
      <p>Early adopters report faster turnaround and sharper insight, yet they also stress the need for clear review steps, shared guidelines and human judgement at every stage.</p>
    </div>
    <footer class="footer"><span>The Truth About AI · Collaborative Report</span><span class="dot"></span></footer>
  </section>

  <!-- Row 3 -->
  <section class="page row-3 quote-page">
    <div class="photo dark" role="img" aria-label="Dark abstract technology scene" style="left:0; top:0; width:160px; height:280px;"></div>
    <blockquote class="pull-quote">“Lorem ipsum dolor sit amet, consectetur adipiscing elit. Sed do eiusmod tempor incididunt ut labore et dolore.”</blockquote>
    <div class="col" style="left:20px; top:300px; width:160px;">
      <p>Brand leaders are rethinking how they plan, create and measure work as machine learning tools move from pilot projects into daily practice. This section outlines what has changed, where the gains are real and which questions teams should ask before they scale new tools across the business.</p>
      <p>Early adopters report faster turnaround and sharper insight, yet they also stress the need for clear review steps, shared guidelines and human judgement at every stage.</p>
    </div>
    <div class="photo" role="img" aria-label="Blue data visualisation" style="left:200px; top:300px; width:192px; height:170px;"></div>
    <div class="col" style="left:200px; top:490px; width:170px;">
      <p>Early adopters report faster turnaround and sharper insight, yet they also stress the need for clear review steps, shared guidelines and human judgement at every stage.</p>
    </div>
    <footer class="footer"><span>The Truth About AI · Collaborative Report</span><span class="dot"></span></footer>
  </section>

  <section class="page row-3 article-a">
    <div class="col" style="left:20px; top:30px; width:160px;">
      <p>Brand leaders are rethinking how they plan, create and measure work as machine learning tools move from pilot projects into daily practice. This section outlines what has changed, where the gains are real and which questions teams should ask before they scale new tools across the business.</p>
      <p>Early adopters report faster turnaround and sharper insight, yet they also stress the need for clear review steps, shared guidelines and human judgement at every stage.</p>
      <p>Brand leaders are rethinking how they plan, create and measure work as machine learning tools move from pilot projects into daily practice. This section outlines what has changed, where the gains are real and which questions teams should ask before they scale new tools across the business.</p>
    </div>
    <div class="col" style="left:206px; top:30px; width:166px;">
      <h3 class="subhead">Sub-heading</h3>
      <p>Early adopters report faster turnaround and sharper insight, yet they also stress the need for clear review steps, shared guidelines and human judgement at every stage.</p>
    </div>
    <div class="photo" role="img" aria-label="Robot hand and human hand with light" style="left:206px; top:170px; width:186px; height:170px;"></div>
    <div class="col" style="left:206px; top:360px; width:166px;">
      <p>Brand leaders are rethinking how they plan, create and measure work as machine learning tools move from pilot projects into daily practice. This section outlines what has changed, where the gains are real and which questions teams should ask before they scale new tools across the business.</p>
    </div>
    <div class="col" style="left:20px; top:400px; width:160px;">
      <p>Early adopters report faster turnaround and sharper insight, yet they also stress the need for clear review steps, shared guidelines and human judgement at every stage.</p>
    </div>
    <footer class="footer"><span>The Truth About AI · Collaborative Report</span><span class="dot"></span></footer>
  </section>

  <section class="page row-3 article-b">
    <div class="col" style="left:20px; top:30px; width:160px;">
      <h3 class="subhead">Sub-heading</h3>
      <p>Early adopters report faster turnaround and sharper insight, yet they also stress the need for clear review steps, shared guidelines and human judgement at every stage.</p>
      <p>Brand leaders are rethinking how they plan, create and measure work as machine learning tools move from pilot projects into daily practice. This section outlines what has changed, where the gains are real and which questions teams should ask before they scale new tools across the business.</p>
      <h3 class="subhead">Sub-heading</h3>
      <p>Early adopters report faster turnaround and sharper insight, yet they also stress the need for clear review steps, shared guidelines and human judgement at every stage.</p>
    </div>
    <div class="photo" role="img" aria-label="Digital face made of light points" style="left:206px; top:20px; width:186px; height:200px;"></div>
    <div class="col" style="left:206px; top:240px; width:166px;">
      <p>Brand leaders are rethinking how they plan, create and measure work as machine learning tools move from pilot projects into daily practice. This section outlines what has changed, where the gains are real and which questions teams should ask before they scale new tools across the business.</p>
      <p>Early adopters report faster turnaround and sharper insight, yet they also stress the need for clear review steps, shared guidelines and human judgement at every stage.</p>
    </div>
    <footer class="footer"><span>The Truth About AI · Collaborative Report</span><span class="dot"></span></footer>
  </section>

  <!-- Row 4 -->
  <section class="page row-4 article-c">
    <div class="col" style="left:20px; top:30px; width:160px;">
      <h3 class="subhead">Sub-heading</h3>
      <p>Brand leaders are rethinking how they plan, create and measure work as machine learning tools move from pilot projects into daily practice. This section outlines what has changed, where the gains are real and which questions teams should ask before they scale new tools across the business.</p>
      <p>Early adopters report faster turnaround and sharper insight, yet they also stress the need for clear review steps, shared guidelines and human judgement at every stage.</p>
    </div>
    <div class="photo" role="img" aria-label="Neural network light trails" style="left:206px; top:30px; width:186px; height:150px;"></div>
    <div class="col" style="left:206px; top:200px; width:166px;">
      <p>Early adopters report faster turnaround and sharper insight, yet they also stress the need for clear review steps, shared guidelines and human judgement at every stage.</p>
    </div>
  </section>

  <section class="page row-4 article-d">
    <div class="photo" role="img" aria-label="Abstract blue technology landscape" style="left:0; top:20px; width:392px; height:130px;"></div>
    <div class="col" style="left:20px; top:170px; width:160px;">
      <h3 class="subhead">Sub-heading</h3>
      <p>Early adopters report faster turnaround and sharper insight, yet they also stress the need for clear review steps, shared guidelines and human judgement at every stage.</p>
    </div>
    <div class="col" style="left:206px; top:170px; width:166px;">
      <p>Brand leaders are rethinking how they plan, create and measure work as machine learning tools move from pilot projects into daily practice. This section outlines what has changed, where the gains are real and which questions teams should ask before they scale new tools across the business.</p>
    </div>
  </section>

  <section class="page row-4 article-e">
    <div class="col" style="left:20px; top:30px; width:160px;">
      <p>Brand leaders are rethinking how they plan, create and measure work as machine learning tools move from pilot projects into daily practice. This section outlines what has changed, where the gains are real and which questions teams should ask before they scale new tools across the business.</p>
      <p>Early adopters report faster turnaround and sharper insight, yet they also stress the need for clear review steps, shared guidelines and human judgement at every stage.</p>
    </div>
    <div class="col" style="left:206px; top:30px; width:166px;">
      <p>Early adopters report faster turnaround and sharper insight, yet they also stress the need for clear review steps, shared guidelines and human judgement at every stage.</p>
      <p>Brand leaders are rethinking how they plan, create and measure work as machine learning tools move from pilot projects into daily practice. This section outlines what has changed, where the gains are real and which questions teams should ask before they scale new tools across the business.</p>
    </div>
  </section>

</main>
</body>
</html>
```